Business Card Design Project

I have just chosen a logo and would now like this designed onto a business card for my hair salon. I would like it to be classy not to busy and have a wow factor when people look at them
Has to Include on card:
Logo Design
And business details below
Kellie-ann Drummond (owner)
0482 736 219
Rdw@vomblet.com.au
71 Willowmere Rise Corvin Cove
Logo is now attached please provide designs
Hair

```html
<!DOCTYPE html>
<html lang="en">
<head>
<meta charset="utf-8">
<title>Velora Hair Studio – Business Card</title>
<link rel="stylesheet" href="https://fonts.googleapis.com/css2?family=Fira+Sans:wght@400;500&display=swap">
<style>
  :root {
    --backdrop: #dcdcdc;
    --card-dark: #343c36;
    --card-teal: #3f6b67;
    --accent-pink: #e2247f;
    --text-light: #ffffff;
  }
  html, body {
    margin: 0;
    padding: 0;
    width: 1200px;
    height: 926px;
    overflow: hidden;
    background: var(--backdrop);
  }
  .canvas {
    position: relative;
    width: 1200px;
    height: 926px;
  }
  .business-card {
    position: absolute;
    left: 220px;
    top: 243px;
    width: 760px;
    height: 440px;
    background: var(--card-dark);
    overflow: hidden;
    font-family: "Fira Sans", sans-serif;
  }
  .business-card__lower-band {
    position: absolute;
    left: 0;
    bottom: 0;
    width: 100%;
    height: 172px;
    background: var(--card-teal);
  }
  .brand-name {
    position: absolute;
    left: 78px;
    top: 112px;
    margin: 0;
    color: var(--accent-pink);
    font-weight: 500;
    font-size: 50px;
    line-height: 1.02;
    letter-spacing: 1px;
    text-transform: uppercase;
  }
  .contact-details {
    position: absolute;
    left: 78px;
    bottom: 30px;
    margin: 0;
    color: var(--text-light);
    font-weight: 400;
    font-size: 21px;
    line-height: 1.3;
    font-style: normal;
  }
  .contact-details span {
    display: block;
  }
</style>
</head>
<body>
  <main class="canvas">
    <section class="business-card" aria-label="Business card front">
      <div class="business-card__lower-band"></div>
      <h1 class="brand-name">Velora<br>Hair Studio</h1>
      <address class="contact-details">
        <span class="contact-details__name">Kellie-ann Drummond</span>
        <span class="contact-details__phone">+ 0482 736 219</span>
        <span class="contact-details__email">Rdw@vomblet.com.au</span>
        <span class="contact-details__address">71 Willowmere Rise Corvin Cove.</span>
      </address>
    </section>
  </main>
</body>
</html>
```